public page kestrel AX (www.kestrelax.com)

https://www.plumaquill.com/shard/s418/sh/b2190ce7-5d3a-4f1e-8c2b-6e7a1d94c0f2/47b1e9c2d0a83f56e1c7b9a2f4d60e81

compatible with wordpress

Designs look the same

Industry/Entity Type

Finance And Accounting

Coding

Coded - Design and coding required

Number of Pages Required

1 page

Font styles to use
Sans Serif

Colors
85cae6
3176b5
cfdeed
fac994
fff3d1
fefdec
cfcfcf
e8e8e8
9d9d9d

```html
<!DOCTYPE html>
<html lang="en">
<head>
<meta charset="utf-8">
<title>kestrel AX – profit for Vendora sellers</title>
<link rel="stylesheet" href="https://fonts.googleapis.com/css2?family=Source+Sans+3:wght@400;600;700&family=Montserrat:wght@500;600;700&display=swap">
<style>
:root{
  --sky:#e3ebf9;
  --blush:#fde7e0;
  --blue:#3176b5;
  --blue-light:#85cae6;
  --ink:#3f4350;
  --text:#55586a;
  --purple:#5b4a8e;
  --peach:#fac994;
  --cream:#fff3d1;
  --salmon:#f8c6b2;
  --coral:#ee8a6b;
  --line:#cfcfcf;
  --grey:#9d9d9d;
  --white:#ffffff;
}
*{box-sizing:border-box;margin:0;padding:0}
html,body{width:1200px;height:4557px;overflow:hidden}
body{position:relative;font-family:"Source Sans 3",sans-serif;color:var(--text);background:var(--blush)}
.abs{position:absolute}
.brand{display:flex;align-items:center;gap:12px;font-family:"Source Sans 3",sans-serif;font-weight:600;font-size:34px;color:var(--blue);letter-spacing:1px}
.brand-dot{width:38px;height:38px;border-radius:50%;background:var(--blue)}

/* top band */
.top{left:0;top:0;width:1200px;height:1338px;background:var(--sky)}
.site-header{left:42px;top:32px;width:1125px;height:60px;display:flex;align-items:center}
.nav{margin-left:auto;display:flex;align-items:center;gap:34px;font-family:"Montserrat",sans-serif;font-size:14px;font-weight:600;color:var(--ink);text-transform:uppercase}
.nav .btn-pill{padding:7px 18px;border-radius:20px;font-size:13px}
.nav .signup{border:2px solid var(--blue);color:var(--blue);margin-left:-10px}
.nav .signin{background:var(--peach);color:var(--ink);margin-left:-20px}
.nav .menu{width:34px;height:34px;background:var(--purple);border-radius:4px;display:flex;flex-direction:column;justify-content:center;gap:5px;padding:0 9px;margin-left:-10px}
.nav .menu span{height:2px;background:var(--white)}

.hero-art{left:0;top:95px;width:600px;height:620px;border-radius:0 0 300px 0;background:radial-gradient(circle at 35% 45%,#f2f6fd 0,#dbe5f6 60%,rgba(227,235,249,0) 100%)}
.hero-title{left:626px;top:236px;width:520px;font-size:36px;line-height:45px;font-weight:700;color:var(--ink)}
.signup-form{display:flex;gap:66px;align-items:center}
.hero-form{left:624px;top:415px}
.field{height:46px;border-radius:23px;background:var(--white);font-size:16px;color:var(--grey);display:flex;align-items:center;padding-left:22px}
.btn{height:46px;border-radius:23px;display:flex;align-items:center;justify-content:center;font-family:"Montserrat",sans-serif;font-weight:600;font-size:15px;color:var(--white)}
.hero-form .field{width:290px}
.hero-form .btn{width:152px;background:var(--blue)}
.watch{left:790px;top:540px;display:flex;align-items:center;gap:12px;font-family:"Montserrat",sans-serif;font-weight:700;font-size:17px;color:var(--ink)}

.pitch{left:0;top:808px;width:1200px;text-align:center}
.pitch h2{font-weight:400;font-size:42px;line-height:50px;color:var(--blue)}
.pitch p{margin:46px auto 0;width:1020px;font-size:19px;line-height:24px;color:var(--ink)}
.pitch b{font-weight:700}
.partners{left:91px;top:1098px;display:flex;gap:36px}
.partner{width:228px;height:132px;background:var(--white);border-radius:6px;box-shadow:0 4px 14px rgba(60,80,130,.12);display:flex;align-items:center;justify-content:center}
.partner span{display:block;width:120px;height:36px;border-radius:6px;background:var(--line)}

/* features */
.wave{left:0;top:1700px;width:1200px;height:900px;background:linear-gradient(170deg,rgba(253,231,224,0) 30%,rgba(245,190,190,.35) 50%,rgba(253,231,224,0) 70%)}
.art{border-radius:24px}
.feature-title{font-size:44px;font-weight:400;color:var(--purple);line-height:50px}
.feature-body{font-size:20px;line-height:26px;color:var(--text);margin-top:16px}

.perks{left:114px;top:3212px;width:972px;display:flex;justify-content:space-between}
.perk{width:300px;text-align:center}
.perk svg{display:block;margin:0 auto 18px}
.perk h3{font-size:20px;font-weight:700;color:var(--purple);margin-bottom:6px}
.perk p{font-size:20px;line-height:25px}

.pricing{left:0;top:3550px;width:1200px;text-align:center}
.pricing h2{font-size:54px;font-weight:400;color:var(--purple);line-height:62px}
.pricing .price{font-size:56px;font-weight:700;color:var(--purple);line-height:64px}
.pricing .btn{width:203px;height:46px;margin:26px auto 0;background:var(--peach);font-size:15px}

.cta{left:94px;top:3866px;width:1012px;height:244px;background:var(--salmon);border:2px solid #f3b39c;border-radius:22px;text-align:center;padding-top:60px}
.cta h2{font-size:34px;font-weight:700;color:var(--ink)}
.cta .signup-form{justify-content:center;gap:12px;margin-top:22px}
.cta .field{width:294px;height:44px}
.cta .btn{width:204px;height:44px;background:var(--purple)}

.site-footer{left:91px;top:4225px;width:1020px;height:300px}
.footer-brand{left:0;top:0}
.socials{left:42px;top:128px;display:flex;gap:22px}
.socials span{width:36px;height:36px;border-radius:50%;background:var(--blue)}
.footer-col h4{font-size:20px;font-weight:700;color:var(--blue);margin-bottom:20px}
.links{left:380px;top:8px}
.links ul{list-style:none;display:grid;grid-template-columns:146px 200px;grid-auto-flow:column;grid-template-rows:repeat(5,29px);font-size:18px;color:var(--text)}
.links li::before{content:"›";color:var(--ink);margin-right:5px}
.contact{left:800px;top:8px}
.contact p{display:flex;align-items:center;gap:8px;font-size:18px;margin-bottom:38px}
.copyright{left:0;top:4505px;width:1200px;text-align:center;font-family:"Montserrat",sans-serif;font-size:10px;font-weight:600;color:var(--ink);letter-spacing:.5px}
</style>
</head>
<body>

<section class="abs top">
  <header class="abs site-header">
    <div class="brand"><span class="brand-dot"></span>KESTREL AX</div>
    <nav class="nav">
      <span>Home</span><span>Pricing</span><span>About</span><span>Contact</span><span>Blog</span><span>FAQs</span>
      <span class="btn-pill signup">Sign up</span>
      <span class="btn-pill signin">Sign in</span>
      <span class="menu"><span></span><span></span><span></span></span>
    </nav>
  </header>

  <div class="abs hero-art" role="img" aria-label="Illustration of a businessman riding a rocket past a globe, coins, charts and a light bulb"></div>
  <h1 class="abs hero-title">We are building a simple and intuitive service for Vendora sellers to calculate their profit</h1>
  <form class="abs signup-form hero-form">
    <div class="field">Your Email Address</div>
    <div class="btn">Get Started</div>
  </form>
  <div class="abs watch">
    <svg width="26" height="26" viewBox="0 0 26 26"><circle cx="13" cy="13" r="11" fill="none" stroke="#3f4350" stroke-width="2"/><path d="M10 8l8 5-8 5z" fill="#3f4350"/></svg>
    WATCH VIDEO
  </div>

  <div class="abs pitch">
    <h2>Profit is not something to add on at the end,<br>it is something to plan for in the beginning</h2>
    <p><b>KESTREL AX</b> is the first ever software created by <b>REAL NEEDS</b> of the <b>REAL VENDORA SELLERS</b> in cooperation with group of brilliant software engineers to help you manage your business and calculate your <b>REAL PROFIT</b> on everyday basis.</p>
  </div>

  <div class="abs partners">
    <div class="partner"><span></span></div>
    <div class="partner"><span></span></div>
    <div class="partner"><span></span></div>
    <div class="partner"><span></span></div>
  </div>
</section>

<div class="abs wave" aria-hidden="true"></div>

<section class="feature">
  <div class="abs art" style="left:137px;top:1444px;width:334px;height:334px;background:radial-gradient(circle,#c9dff3 0,#f2d6cf 70%,rgba(253,231,224,0) 100%)" role="img" aria-label="Illustration of a hand holding a magnifying glass surrounded by connected icons"></div>
  <div class="abs" style="left:538px;top:1522px;width:580px">
    <h2 class="feature-title">Find new keywords</h2>
    <p class="feature-body">Lorem ipsum dolor sit amet, consectetur adipiscing elit, sed do eiusmod tempor incididunt ut labore et dolore magna aliqua. Ut enim ad minim veniam, quis nos trud exercitation ullamco laboris nisi ut aliquip.</p>
  </div>
</section>

<section class="feature">
  <div class="abs" style="left:143px;top:1942px;width:400px">
    <h2 class="feature-title">Boost your sales</h2>
    <p class="feature-body">Lorem ipsum dolor sit amet, consectetur adipiscing elit, sed do eiusmod tempor incididunt ut labore et dolore magna ali qua ut enim ad minim veniam.</p>
  </div>
  <div class="abs art" style="left:562px;top:1885px;width:520px;height:305px;background:linear-gradient(160deg,#d9e4f4,#f0cfc9)" role="img" aria-label="Illustration of a group of people holding coin signs and a brand banner beside a piggy bank"></div>
</section>

<section class="feature">
  <div class="abs art" style="left:137px;top:2280px;width:365px;height:245px;background:linear-gradient(150deg,#3d6c86,#b9d0df)" role="img" aria-label="Illustration of a laptop showing dashboards with a hand clicking a mouse"></div>
  <div class="abs" style="left:593px;top:2355px;width:520px">
    <h2 class="feature-title">Automate PPC Campaign</h2>
    <p class="feature-body">Lorem ipsum dolor sit amet, consectetur adipis cing elit, sed do eiusmod tempor incididunt ut la bore et dolore magna aliqua. Ut enim ad minim veniam, quis nos trud exercitation.</p>
  </div>
</section>

<section class="feature">
  <div class="abs" style="left:143px;top:2772px;width:400px">
    <h2 class="feature-title">Success and make<br>profit on Vendora</h2>
    <p class="feature-body">Lorem ipsum dolor sit amet, consecte tur adipiscing elit, sed do eiusmod tempor incididu ut labore et dolore magna aliqua.</p>
  </div>
  <div class="abs art" style="left:562px;top:2675px;width:472px;height:365px;background:linear-gradient(170deg,#8e9aa8,#e86a55 60%,#f5c98b)" role="img" aria-label="Illustration of a rocket launching from a laptop store page with a hand holding a phone"></div>
</section>

<section class="abs perks">
  <div class="perk">
    <svg width="70" height="64" viewBox="0 0 70 64" fill="none" stroke="#ee8a6b" stroke-width="3"><rect x="6" y="40" width="10" height="20"/><rect x="22" y="30" width="10" height="30"/><rect x="38" y="22" width="10" height="38"/><rect x="54" y="12" width="10" height="48"/><path d="M4 30 L26 16 L42 20 L64 4"/></svg>
    <h3>Complete Data Analytics</h3>
    <p>Lorem ipsum dolor sit amet, consectetur adipiscing elit, sed do eiusmod tempor inci didu ut labore et dolore.</p>
  </div>
  <div class="perk">
    <svg width="70" height="64" viewBox="0 0 70 64" fill="none" stroke="#ee8a6b" stroke-width="3"><rect x="10" y="4" width="50" height="56" rx="4"/><rect x="24" y="30" width="22" height="18" rx="2"/><path d="M28 30v-6a7 7 0 0 1 14 0v6"/></svg>
    <h3>Security and Privacy</h3>
    <p>Lorem ipsum dolor sit amet, consectetur adipiscing elit, sed do eiusmod tempor inci didu ut labore et dolore.</p>
  </div>
  <div class="perk">
    <svg width="70" height="64" viewBox="0 0 70 64" fill="none" stroke="#ee8a6b" stroke-width="3"><path d="M12 34v-6a23 23 0 0 1 46 0v6"/><rect x="6" y="32" width="10" height="16" rx="3"/><rect x="54" y="32" width="10" height="16" rx="3"/><path d="M59 48c0 8-8 12-18 12"/></svg>
    <h3>Expert Support</h3>
    <p>Lorem ipsum dolor sit amet, consectetur adipiscing elit, sed do eiusmod tempor inci didu ut labore et dolore.</p>
  </div>
</section>

<section class="abs pricing">
  <h2>Complete analytics solutions only</h2>
  <p class="price">$2.95/month*</p>
  <div class="btn">Get Started</div>
</section>

<section class="abs cta">
  <h2>Try Kestrel AX now and start calculating your profit</h2>
  <form class="signup-form">
    <div class="field">Your Email Address</div>
    <div class="btn">Get Started</div>
  </form>
</section>

<footer class="abs site-footer">
  <div class="abs footer-brand brand"><span class="brand-dot"></span>KESTREL AX</div>
  <div class="abs socials"><span></span><span></span><span></span><span></span></div>
  <div class="abs footer-col links">
    <h4>Quick Links</h4>
    <ul>
      <li>Home</li><li>Pricing</li><li>About Us</li><li>Contact</li><li>Blog</li>
      <li>FAQs</li><li>Sign Up</li><li>Sign In</li><li>Privacy Policy</li><li>Terms &amp; Conditions</li>
    </ul>
  </div>
  <div class="abs footer-col contact">
    <h4>Contact</h4>
    <p><svg width="18" height="18" viewBox="0 0 18 18" fill="none" stroke="#55586a" stroke-width="1.6"><circle cx="9" cy="9" r="8"/><path d="M6 5l2 2-1 1.5c.8 1.5 1.7 2.4 3 3L11.5 10l2 2-1.5 1.5C9 13 5.5 9.5 4.5 6.5z"/></svg>+1 555-013-0427</p>
    <p><svg width="18" height="18" viewBox="0 0 18 18" fill="none" stroke="#55586a" stroke-width="1.6"><circle cx="9" cy="9" r="8"/><path d="M4.5 6.5h9v6h-9zM4.5 6.5L9 10l4.5-3.5"/></svg>info@kestrelax.com</p>
  </div>
</footer>
<p class="abs copyright">COPYRIGHT © 2018 KESTRELAX. ALL RIGHTS RESERVED</p>

</body>
</html>
```